Web Design Project - Investor Services

I would like a simple and elegant web design for my company "Torvelo Management". The company will provide services to Corporate and Institutional investors for their needs with local/foreign investment vehicles. The website will have four pages to start: home, about us, services, contact.
I already chose a logo, and I will attach the source file. The color that I will most probably use for the logo will be blue, and i also like grey with a white background. For the website I would like to see light colors, maybe light green or grey, with the logo either in blue, grey or white (depeding on the background).
Target Market(s)
Investment managers and tax/legal advisors from top firms. This is the reason why I want something simple and elegant.
Industry/Entity Type
Investment
Requirements
Nice to have
- I do not want many pictures in the website, but I might include a couple of pictures of Madrid and maybe a picture of myself in the about us page (still deciding). I will attach some pictures of Madrid that I like, but feel free to search for others - i have others but i am not able to attach all of them.

```html
<!DOCTYPE html>
<html lang="en">
<head>
<meta charset="utf-8">
<title>Torvelo Management</title>
<link rel="stylesheet" href="https://fonts.googleapis.com/css2?family=Carlito:wght@400;700&family=Arimo:wght@400&display=swap">
<style>
  :root {
    --ink: #000000;
    --paper: #ffffff;
    --text: #1a1a1a;
    --muted: #666666;
    --nav-muted: #6e6e6e;
    --panel: #d4d4d4;
    --field-border: #b5b5b5;
    --button-face: #e9e9e9;
    --sky-top: #c9ccd1;
    --sky-mid: #aab0b8;
    --city-low: #3c4240;
    --city-deep: #232624;
  }
  * { margin: 0; padding: 0; box-sizing: border-box; }
  html, body { width: 1200px; height: 1000px; overflow: hidden; background: var(--paper); }
  body { position: relative; font-family: "Carlito", "Calibri", sans-serif; color: var(--text); }

  .top-bar { position: absolute; left: 0; top: 0; width: 1200px; height: 31px; background: var(--ink); }

  .brand {
    position: absolute; left: 209px; top: 31px; width: 172px; height: 79px;
    background: var(--ink); color: var(--paper);
    display: flex; align-items: center; justify-content: center;
    font-size: 17px; font-weight: 400; letter-spacing: 0.2px;
  }

  .main-nav { position: absolute; top: 86px; left: 0; font-family: "Arimo", Arial, sans-serif; font-size: 14px; }
  .main-nav a { position: absolute; white-space: nowrap; color: var(--nav-muted); text-decoration: none; }
  .main-nav a.current { color: var(--ink); }

  .search { position: absolute; left: 839px; top: 81px; display: flex; gap: 3px; }
  .search-field { width: 111px; height: 23px; border: 1px solid var(--field-border); background: var(--paper); }
  .search-button {
    width: 56px; height: 23px; border: 1px solid var(--field-border); background: var(--button-face);
    font-family: "Arimo", Arial, sans-serif; font-size: 12px; color: var(--ink);
    display: flex; align-items: center; justify-content: center;
  }

  .hero-shadow {
    position: absolute; left: 230px; top: 395px; width: 800px; height: 60px;
    background: radial-gradient(ellipse at 50% 20%, rgba(0,0,0,0.75) 0%, rgba(0,0,0,0.35) 45%, rgba(0,0,0,0) 72%);
  }
  .hero-image {
    position: absolute; left: 209px; top: 110px; width: 800px; height: 302px;
    background: linear-gradient(180deg, var(--sky-top) 0%, var(--sky-mid) 55%, #7d8088 72%, var(--city-low) 88%, var(--city-deep) 100%);
  }
  .hero-caption {
    position: absolute; left: 226px; top: 167px; width: 335px; height: 194px;
    background: rgba(235, 235, 235, 0.78);
    padding: 62px 20px 0 32px;
    font-size: 24px; font-weight: 700; line-height: 30px; color: var(--ink);
  }

  .welcome-title { position: absolute; left: 214px; top: 453px; font-size: 16px; color: var(--ink); }
  .welcome-text {
    position: absolute; left: 214px; top: 498px; width: 790px;
    font-size: 11.4px; line-height: 15px; color: var(--muted);
  }

  .feature-panel { position: absolute; left: 209px; top: 584px; width: 800px; height: 274px; background: var(--panel); }
  .feature { position: absolute; top: 0; height: 274px; }
  .feature-head { position: absolute; top: 8px; display: flex; align-items: center; gap: 4px; font-size: 16px; color: var(--ink); white-space: nowrap; }
  .feature-head svg { display: block; }
  .feature-body { position: absolute; top: 50px; font-size: 11.8px; line-height: 15px; color: var(--ink); }
  .feature-body p + p { margin-top: 12px; }
  .learn-more {
    position: absolute; top: 248px; width: 73px; height: 19px; background: var(--ink); color: var(--paper);
    font-size: 11.5px; display: flex; align-items: center; justify-content: center; text-decoration: none;
  }

  .social { position: absolute; top: 885px; left: 868px; display: flex; gap: 27px; }
  .social span { width: 16px; height: 16px; border-radius: 50%; background: var(--ink); display: block; }

  .site-footer { position: absolute; left: 0; top: 905px; width: 1200px; height: 95px; background: var(--ink); color: var(--paper); }
  .footer-nav { font-family: "Arimo", Arial, sans-serif; font-size: 12px; }
  .footer-nav a { position: absolute; top: 23px; color: var(--paper); text-decoration: none; white-space: nowrap; }
  .copyright { position: absolute; top: 59px; left: 0; width: 1206px; text-align: center; font-size: 11.5px; }
</style>
</head>
<body>
  <div class="top-bar"></div>

  <header>
    <div class="brand">Torvelo Management</div>
    <nav class="main-nav">
      <a class="current" href="#" style="left:417px">HOME</a>
      <a href="#" style="left:494px">ABOUT US</a>
      <a href="#" style="left:604px">SERVICES</a>
      <a href="#" style="left:712px">CONTACT US</a>
    </nav>
    <div class="search">
      <div class="search-field"></div>
      <div class="search-button">Search</div>
    </div>
  </header>

  <div class="hero-shadow"></div>
  <div class="hero-image" role="img" aria-label="Photograph of the Madrid skyline with its business district towers"></div>
  <div class="hero-caption">Lorem ipsum dolor sit amet, consectetur p ex ea commodo consequat.</div>

  <h1 class="welcome-title" style="font-weight:400">Welcome to our site</h1>
  <p class="welcome-text">Lorem ipsum dolor sit amet, consectetur adipisicing elit, sed do eiusmod tempor incididunt ut labore et dolore magna aliqua. Ut enim ad minim veniam, quis nostrud exercitation ullamco laboris nisi ut aliquip ex ea commodo consequat. Duis aute irure dolor in reprehenderit in voluptate velit esse cillum dolore eu fugiat nulla pariatur. Excepteur sint occaecat cupidatat non proident, sunt in culpa qui officia deserunt mollit anim id est laborum.</p>

  <section class="feature-panel">
    <div class="feature" style="left:28px">
      <h2 class="feature-head" style="font-weight:400">
        <svg width="28" height="26" viewBox="0 0 28 26" aria-hidden="true">
          <circle cx="14" cy="8" r="6" fill="#6b6b6b"/>
          <path d="M2 26 C2 17 8 14 14 14 C20 14 26 17 26 26 Z" fill="#7a7a7a"/>
        </svg>
        About us
      </h2>
      <div class="feature-body" style="left:1px; width:212px">
        <p>Lorem ipsum dolor sit amet, consectetur adipisicing elit, sed do eiusmod tempor incididunt ut labore et dolore magna aliqua. Ut enim ad minim veniam, quis nostrud exercitation ullamco laboris nisi ut aliquip ex ea commodo consequat. Duis aute irure dolor in reprehenderit in voluptate velit esse cillum dolore eu fugiat nulla pariatur. Excepteur sint occaecat cupidatat non proident, sunt in culpa qui officia deserunt mollit anim id est laborum.</p>
      </div>
      <a class="learn-more" href="#" style="left:132px">Learn more</a>
    </div>

    <div class="feature" style="left:299px">
      <h2 class="feature-head" style="font-weight:400">
        <svg width="28" height="26" viewBox="0 0 28 26" aria-hidden="true">
          <g fill="#6b6b6b">
            <circle cx="14" cy="13" r="9"/>
            <rect x="12" y="1" width="4" height="5"/>
            <rect x="12" y="20" width="4" height="5"/>
            <rect x="2" y="11" width="5" height="4"/>
            <rect x="21" y="11" width="5" height="4"/>
          </g>
          <circle cx="14" cy="13" r="3.5" fill="#d4d4d4"/>
        </svg>
        Services
      </h2>
      <div class="feature-body" style="left:4px; width:215px">
        <p>Lorem ipsum dolor sit amet, consectetur adipisicing elit, sed do eiusmod tempor.</p>
        <p>Lorem ipsum dolor sit amet, consectetur adipisicing elit, sed do eiusmod tempor.</p>
        <p>Lorem ipsum dolor sit amet, consectetur adipisicing elit, sed do eiusmod tempor.</p>
        <p>Lorem ipsum dolor sit amet, consectetur adipisicing elit, sed do eiusmod tempor.</p>
      </div>
      <a class="learn-more" href="#" style="left:137px">Learn more</a>
    </div>

    <div class="feature" style="left:564px">
      <h2 class="feature-head" style="font-weight:400">
        <svg width="32" height="26" viewBox="0 0 32 26" aria-hidden="true">
          <ellipse cx="12" cy="10" rx="11" ry="8" fill="#7a7a7a"/>
          <path d="M6 16 L4 23 L11 17 Z" fill="#7a7a7a"/>
          <ellipse cx="21" cy="14" rx="10" ry="7" fill="#9a9a9a"/>
          <path d="M25 19 L29 25 L21 20 Z" fill="#9a9a9a"/>
        </svg>
        Client Testimonials
      </h2>
      <div class="feature-body" style="left:3px; width:212px">
        <p>Lorem ipsum dolor sit amet, consectetur adipisicing elit, sed do eiusmod tempor incididunt ut labore et dolore magna aliqua. Ut enim ad minim veniam, quis nostrud exercitation ullamco laboris nisi ut aliquip ex ea commodo consequat. Duis aute irure dolor in reprehenderit in voluptate velit esse cillum dolore eu fugiat nulla pariatur. Excepteur sint occaecat cupidatat non proident, sunt in culpa qui officia deserunt mollit anim id est laborum.</p>
      </div>
      <a class="learn-more" href="#" style="left:137px">Learn more</a>
    </div>
  </section>

  <div class="social" aria-label="Social links">
    <span></span><span></span><span></span><span></span>
  </div>

  <footer class="site-footer">
    <nav class="footer-nav">
      <a href="#" style="left:449px">HOME</a>
      <a href="#" style="left:513px">ABOUT US</a>
      <a href="#" style="left:605px">SERVICES</a>
      <a href="#" style="left:695px">CONTACT US</a>
    </nav>
    <p class="copyright">Copyright © 2013 Torvelo</p>
  </footer>
</body>
</html>
```